Velko
trosen
Use same font as used in my logo
Yousef Harbi يوسف حربي
General manager المدير العام
P.O.Box 48735 Riyadh 13542
Saudi Arabia
ص.ب 48735 الرياض 13542
المملكة العربية السعودية
Info@velkohouse.example
www.velkohouse.example
C.R. 1049728513 CC.487139
I want to be design Arabic & English

```html
<!DOCTYPE html>
<html lang="en">
<head>
<meta charset="utf-8">
<title>Velko House — Business Card</title>
<link rel="stylesheet" href="https://fonts.googleapis.com/css2?family=Open+Sans:wght@400;600;700&family=Cairo:wght@400;600;700&display=swap">
<style>
  :root {
    --stage: #e6e8eb;
    --card: #ffffff;
    --card-shade: #eef1f4;
    --brand: #1d5c8c;
    --brand-dark: #164a72;
    --brand-light: #3f7fae;
    --ink-soft: #7a8088;
    --on-brand: #ffffff;
  }
  * { box-sizing: border-box; margin: 0; padding: 0; }
  html, body { width: 1200px; height: 901px; overflow: hidden; }
  body {
    background: var(--stage);
    font-family: "Open Sans", Arial, sans-serif;
    position: relative;
  }
  .card {
    position: absolute;
    left: 240px;
    width: 720px;
    height: 411px;
    border-radius: 22px;
    overflow: hidden;
    background: linear-gradient(180deg, var(--card) 0%, var(--card-shade) 100%);
    box-shadow: 0 8px 24px rgba(0,0,0,.15);
  }
  .card--arabic { top: 26px; }
  .card--english { top: 464px; }

  .brand {
    position: absolute;
    left: 44px;
    top: 46px;
    display: flex;
    align-items: center;
    gap: 16px;
  }
  .brand__mark {
    width: 58px; height: 58px;
    border-radius: 50%;
    border: 5px solid var(--brand);
  }
  .brand__name {
    font-family: "Open Sans", Arial, sans-serif;
    font-weight: 600;
    font-size: 40px;
    letter-spacing: 1px;
    color: var(--brand);
  }

  .band {
    position: absolute;
    left: 0; right: 0;
    top: 152px;
    height: 150px;
    background: linear-gradient(100deg, var(--brand-light) 0%, var(--brand) 30%, var(--brand-dark) 100%);
  }

  .contact {
    position: absolute;
    left: 44px;
    top: 166px;
    color: var(--on-brand);
    font-size: 14px;
    line-height: 19px;
  }
  .contact__address { margin-bottom: 10px; }
  .contact__line { display: flex; align-items: center; gap: 8px; }
  .contact__line svg { width: 14px; height: 14px; flex: none; }

  .person {
    position: absolute;
    left: 340px;
    top: 222px;
    color: var(--on-brand);
  }
  .person__name { font-size: 23px; font-weight: 700; line-height: 28px; }
  .person__role { font-size: 14px; }

  .emblem {
    position: absolute;
    right: -40px;
    top: 196px;
    width: 220px; height: 220px;
    border-radius: 50%;
    background: radial-gradient(circle, rgba(29,92,140,.55) 0%, rgba(29,92,140,.25) 70%, rgba(29,92,140,.1) 100%);
  }

  .web {
    position: absolute;
    left: 44px;
    bottom: 36px;
    font-size: 14px;
    letter-spacing: 3px;
    color: var(--ink-soft);
  }
  .rule {
    position: absolute;
    left: 44px;
    width: 380px;
    bottom: 28px;
    height: 1px;
    background: #cfd4da;
  }

  .card--arabic .contact,
  .card--arabic .person { font-family: "Cairo", Arial, sans-serif; }
  .card--arabic .contact__address { direction: rtl; text-align: right; }
  .card--arabic .person { direction: rtl; text-align: right; left: auto; right: 240px; top: 186px; }
  .card--arabic .person__name { font-size: 20px; }
</style>
</head>
<body>

<svg width="0" height="0" style="position:absolute" aria-hidden="true">
  <symbol id="icon-phone" viewBox="0 0 16 16"><path fill="#fff" d="M3 1h3l1 4-2 1c1 2 3 4 5 5l1-2 4 1v3c0 1-1 2-2 2C7 15 1 9 1 3c0-1 1-2 2-2z"/></symbol>
  <symbol id="icon-mobile" viewBox="0 0 16 16"><rect x="4" y="1" width="8" height="14" rx="1.5" fill="#fff"/><rect x="5.5" y="3" width="5" height="8" fill="#1d5c8c"/></symbol>
  <symbol id="icon-fax" viewBox="0 0 16 16"><rect x="4" y="1" width="8" height="5" fill="#fff"/><rect x="1" y="6" width="14" height="7" rx="1" fill="#fff"/><rect x="4" y="10" width="8" height="5" fill="#fff" stroke="#1d5c8c"/></symbol>
  <symbol id="icon-mail" viewBox="0 0 16 16"><rect x="1" y="3" width="14" height="10" rx="1" fill="#fff"/><path d="M1.5 3.5 8 9l6.5-5.5" fill="none" stroke="#1d5c8c" stroke-width="1.3"/></symbol>
</svg>

<section class="card card--arabic" lang="ar">
  <div class="brand">
    <span class="brand__mark"></span>
    <span class="brand__name" lang="en">VELKO HOUSE</span>
  </div>
  <div class="band"></div>
  <div class="contact">
    <p class="contact__address">ص.ب 48735 الرياض 13542<br>المملكة العربية السعودية</p>
    <p class="contact__line" lang="en"><svg><use href="#icon-phone"/></svg>+96655218407</p>
    <p class="contact__line" lang="en"><svg><use href="#icon-mobile"/></svg>+96614870265</p>
    <p class="contact__line" lang="en"><svg><use href="#icon-fax"/></svg>+96614870265</p>
    <p class="contact__line" lang="en"><svg><use href="#icon-mail"/></svg>Info@velkohouse.example</p>
  </div>
  <div class="person">
    <p class="person__name">يوسف حربي</p>
    <p class="person__role">المدير العام</p>
  </div>
  <div class="emblem" role="img" aria-label="Large Velko House emblem decoration"></div>
  <p class="web" lang="en">www.velkohouse.example</p>
  <div class="rule"></div>
</section>

<section class="card card--english">
  <div class="brand">
    <span class="brand__mark"></span>
    <span class="brand__name">VELKO HOUSE</span>
  </div>
  <div class="band"></div>
  <div class="contact">
    <p class="contact__address">P.O.Box 48735 Riyadh 13542<br>Saudi Arabia</p>
    <p class="contact__line"><svg><use href="#icon-phone"/></svg>+96655218407</p>
    <p class="contact__line"><svg><use href="#icon-mobile"/></svg>+96614870265</p>
    <p class="contact__line"><svg><use href="#icon-fax"/></svg>+96614870265</p>
    <p class="contact__line"><svg><use href="#icon-mail"/></svg>Info@velkohouse.example</p>
  </div>
  <div class="person">
    <p class="person__name">Yousef Harbi</p>
    <p class="person__role">General manager</p>
  </div>
  <div class="emblem" role="img" aria-label="Large Velko House emblem decoration"></div>
  <p class="web">www.velkohouse.example</p>
  <div class="rule"></div>
</section>

</body>
</html>
```